Purchasing community for life science startups needs landing page for collecting of contact adresses

We are the "Pipette Union", the first purchasing community for life science startups. The idea is to bundle the needs of several smaller companies (laboratories) and to buy lab consumables and chemicals in larger quantities. This bargaining position, at the end of all participants can buy their products very low prices. In the attached powerpoint file you will find an idea and some elements, which demonstrate a little the style, which came into my mind.
Urlaub/Ferien
Target Market(s)
Our target customers are startups and smaller biotech companies, which are too small to get the best prices. The aim of this landing page is to collect all interested parties.
Look and feel

```html
<!DOCTYPE html>
<html lang="de">
<head>
<meta charset="utf-8">
<title>Pipette Union – Einkaufsgemeinschaft LifeScience</title>
<link href="https://fonts.googleapis.com/css2?family=Raleway:ital,wght@0,400;0,500;0,600;0,700;1,400&display=swap" rel="stylesheet">
<style>
  :root {
    --orange: #e8620f;
    --orange-dark: #b8460a;
    --ink: #1d1d1d;
    --text: #6c6c6c;
    --muted: #8e8e8e;
    --panel: #e4e4e4;
    --white: #ffffff;
    --icon-grey: #8a8a8a;
    --social-grey: #d0d0d0;
  }
  * { box-sizing: border-box; margin: 0; padding: 0; }
  html, body { width: 1200px; height: 1200px; overflow: hidden; }
  body { background: var(--white); font-family: "Raleway", sans-serif; color: var(--ink); position: relative; }

  .page {
    position: absolute; left: 130px; top: 28px; width: 939px; height: 1150px;
    background: var(--white);
    box-shadow: 0 0 40px rgba(0,0,0,0.22);
  }
  section, footer { position: absolute; left: 0; width: 100%; }

  /* Hero */
  .hero { top: 0; height: 352px; border: 1px solid var(--orange); overflow: hidden; }
  .hero-art {
    position: absolute; left: 18px; top: 38px; width: 920px; height: 300px;
    background: radial-gradient(ellipse at 55% 60%, #fbe1cc 0%, #fdf1e7 45%, #ffffff 75%);
  }
  .hamburger { position: absolute; left: 822px; top: 42px; width: 34px; height: 24px; }
  .hamburger span { display: block; height: 5px; background: var(--orange); border-radius: 2px; margin-bottom: 4.5px; }
  .brand { position: absolute; left: 69px; top: 96px; display: flex; align-items: flex-start; }
  .brand-square { width: 71px; height: 71px; background: var(--orange-dark); }
  .brand-text { margin-left: 4px; margin-top: -3px; }
  .brand-name { font-size: 30px; font-weight: 700; letter-spacing: 0.2px; color: var(--ink); line-height: 1.1; text-transform: uppercase; }
  .brand-tag { font-size: 16px; font-weight: 400; color: var(--ink); line-height: 1.1; }
  .store-links { position: absolute; left: 255px; top: 169px; display: flex; gap: 10px; }
  .store-links span { width: 30px; height: 30px; border-radius: 50%; background: var(--icon-grey); }
  .store-links span.active { background: var(--orange); }

  /* Features */
  .features { top: 352px; height: 196px; display: flex; justify-content: center; border-bottom: 1px solid var(--orange); }
  .feature { position: absolute; top: 36px; width: 230px; text-align: center; }
  .feature-icon { width: 58px; height: 58px; border-radius: 50%; background: var(--orange); margin: 0 auto; display: flex; align-items: center; justify-content: center; }
  .feature h3 { margin-top: 13px; font-size: 13.5px; font-weight: 600; }
  .feature p { margin-top: 12px; font-size: 9.5px; line-height: 15px; color: var(--text); }

  /* Notify */
  .notify { top: 548px; height: 250px; background: var(--panel); border-bottom: 1px solid var(--orange); }
  .notify h2 { position: absolute; left: 123px; top: 33px; font-size: 13px; font-weight: 500; }
  .notify p { position: absolute; left: 123px; top: 60px; width: 318px; font-size: 9.4px; line-height: 15.2px; color: var(--text); }
  .signup { position: absolute; left: 123px; top: 134px; display: flex; height: 33px; }
  .signup .email { width: 179px; background: var(--white); border: 1px solid #d2d2d2; border-right: 0; border-radius: 6px 0 0 6px; font: 400 10.5px "Raleway", sans-serif; color: var(--muted); padding-left: 14px; display: flex; align-items: center; }
  .signup .notify-btn { width: 83px; background: var(--orange); color: var(--white); border-radius: 0 6px 6px 0; font-size: 13px; font-weight: 600; display: flex; align-items: center; justify-content: center; }
  .video { position: absolute; left: 522px; top: 37px; width: 294px; height: 180px; border-radius: 3px; overflow: hidden;
    background: radial-gradient(ellipse at 50% 35%, #e8eef2 0%, #a9bccb 55%, #5b7387 100%); }
  .video-controls { position: absolute; left: 12px; bottom: 12px; width: 270px; height: 24px; background: rgba(40,40,40,0.8); border-radius: 2px; }
  .video-controls .play { position: absolute; left: 0; top: 0; width: 36px; height: 24px; background: #2a2a2a; }
  .video-controls .track { position: absolute; left: 60px; top: 10px; width: 150px; height: 4px; background: #555; }
  .video-controls .track i { display: block; width: 95px; height: 4px; background: #29a4e0; }

  /* Testimonial & contact */
  .voices { top: 800px; height: 272px; text-align: center; border-bottom: 1px solid var(--orange); }
  .quote { position: absolute; left: 0; width: 100%; top: 31px; font-size: 10.6px; line-height: 17.6px; font-style: italic; color: var(--text); }
  .author { position: absolute; left: 0; width: 100%; top: 75px; font-size: 10.5px; font-weight: 700; }
  .members { position: absolute; left: 134px; top: 102px; width: 664px; height: 30px;
    background: linear-gradient(90deg, #e9d3c2, #b58d74, #d9b49c, #7e6152, #e2c4ae, #a88a7a, #d7bba8); }
  .voices h2 { position: absolute; left: 0; width: 100%; top: 164px; font-size: 14px; font-weight: 500; }
  .voices .lead { position: absolute; left: 0; width: 100%; top: 191px; font-size: 9.5px; color: var(--text); }
  .social { position: absolute; left: 395px; top: 218px; display: flex; gap: 6px; }
  .social span { width: 20px; height: 20px; border-radius: 50%; background: var(--social-grey); }
  .social span.active { background: var(--orange); }

  /* Footer */
  .site-footer { top: 1073px; height: 77px; background: var(--panel); display: flex; justify-content: center; align-items: center; gap: 19px; }
  .site-footer a { font-size: 10px; color: var(--text); text-decoration: none; }
</style>
</head>
<body>
<main class="page">

  <section class="hero">
    <div class="hero-art" role="img" aria-label="Orange computer mouse whose cable forms a shopping cart and ends in a USB plug"></div>
    <div class="hamburger" aria-label="Menu"><span></span><span></span><span></span></div>
    <div class="brand">
      <div class="brand-square"></div>
      <div class="brand-text">
        <div class="brand-name">Pipette Union</div>
        <div class="brand-tag">Einkaufsgemeinschaft LifeScience</div>
      </div>
    </div>
    <div class="store-links"><span></span><span></span><span class="active"></span></div>
  </section>

  <section class="features">
    <div class="feature" style="left:101px">
      <div class="feature-icon">
        <svg width="26" height="26" viewBox="0 0 24 24"><g fill="#fff"><circle cx="12" cy="12" r="7"/><g stroke="#fff" stroke-width="3.2" stroke-linecap="round"><line x1="12" y1="2" x2="12" y2="22"/><line x1="2" y1="12" x2="22" y2="12"/><line x1="5" y1="5" x2="19" y2="19"/><line x1="19" y1="5" x2="5" y2="19"/></g></g><circle cx="12" cy="12" r="3" fill="#e8620f"/></svg>
      </div>
      <h3>Lorem ipsum</h3>
      <p>Lorem ipsum dolor sit amet, consectetur<br>adipiscing elit. Suspendisse fringilla fringilla.</p>
    </div>
    <div class="feature" style="left:353px">
      <div class="feature-icon">
        <svg width="28" height="28" viewBox="0 0 24 24"><polygon fill="#fff" points="12,1.5 15,8.7 22.8,9.3 16.8,14.4 18.7,22 12,17.9 5.3,22 7.2,14.4 1.2,9.3 9,8.7"/></svg>
      </div>
      <h3>Lorem ipsum</h3>
      <p>Lorem ipsum dolor sit amet, consectetur<br>adipiscing elit. Suspendisse fringilla fringilla.</p>
    </div>
    <div class="feature" style="left:605px">
      <div class="feature-icon">
        <svg width="28" height="28" viewBox="0 0 24 24"><circle cx="12" cy="12" r="9.5" fill="none" stroke="#fff" stroke-width="2.4"/><path fill="#fff" d="M7 8c2-1 3 1 4 2s0 3-1 3-1 2-2 3c-1-2-2-5-1-8zM13 6c2 0 4 1 5 3-1 1-2 0-3 1s1 3 0 4-2 1-3-1 1-3 0-4-1-2 1-3z"/></svg>
      </div>
      <h3>Lorem ipsum</h3>
      <p>Lorem ipsum dolor sit amet, consectetur<br>adipiscing elit. Suspendisse fringilla fringilla.</p>
    </div>
  </section>

  <section class="notify">
    <h2>Get Notified Of Any Updates!</h2>
    <p>Lorem ipsum dolor sit amet, consectetur adipiscing elit. Suspendisse fringilla fringilla nisl congue congue. Maecenas nec condimentum libero, at elementum mauris. Phasellus eget nisi dapibus, ultricies nisl at, hendrerit risusuis ornare luctus id sollicitudin ante lobortis at.</p>
    <div class="signup">
      <div class="email">Email Address</div>
      <div class="notify-btn">Notify</div>
    </div>
    <div class="video" role="img" aria-label="Video still: shopping cart and goldfish leaping out of a laptop screen">
      <div class="video-controls">
        <div class="play"><svg width="36" height="24" viewBox="0 0 36 24"><polygon points="14,7 23,12 14,17" fill="#fff"/></svg></div>
        <div class="track"><i></i></div>
      </div>
    </div>
  </section>

  <section class="voices">
    <p class="quote">“Lorem ipsum dolor sit amet, consectetur adipiscing elit. Mauris interdum velit vitae nulla molestie eu<br>commodo nulla dapib us. Donec id sollicitudin urna. Integer at dui ac leo fermentum varius eleifend ut.”</p>
    <p class="author">John Doe</p>
    <div class="members" role="img" aria-label="Row of member portrait photos"></div>
    <h2>Say Hi &amp; Get in Touch</h2>
    <p class="lead">Lorem ipsum dolor sit amet, consectetur adipiscing elit suspendisse.</p>
    <div class="social"><span></span><span></span><span class="active"></span><span></span><span></span><span></span></div>
  </section>

  <footer class="site-footer">
    <a href="#">Contact</a>
    <a href="#">Download</a>
    <a href="#">Press</a>
    <a href="#">Email</a>
    <a href="#">Support</a>
    <a href="#">Privacy Policy</a>
  </footer>

</main>
</body>
</html>
```